OLVAK Web Design (Need help to re-design our website)

We need someone to help us re-design our website and launch it. All contents for the website are ready. (https://olvak.example.au/)

-Rearrange categories:
1. Heating & Cooling
2. Remove Home Appliance
3. Remove Entertainment

Home page - redesign (It will be a nice touch if the banner is in the loop).

NOTE:
-Brand colour blue and orange.
-Try using professional fonts (Example: Helvetica, etc.)
-The website's Footer should be readable and use light colour.

Target Market(s)

Residentials & commercial buildings

Industry/Entity Type

Heat Ventilation and Cooling Industry, Technology , Renewables

Coding

Coded - Design and coding required

Colors
0094D4
00A9DD
6FCCEA
C7EBF8
E9F6FB
59FF00
82FF00
B8FF75
E3FFCB
F4FFEA
F0912C
F2A743
F7CA91
FBE8D2
FDF5EE

Requirements
Nice to have
• Effects/transition on the words/copy/images.

```html
<!DOCTYPE html>
<html lang="en">
<head>
<meta charset="utf-8">
<title>OLVAK — Heating, Cooling &amp; Energy Solutions</title>
<link href="https://fonts.googleapis.com/css2?family=Poppins:wght@500;600;700&family=Jost:wght@300;400;500&display=swap" rel="stylesheet">
<style>
:root{
  --blue:#1a60b5;
  --blue-dark:#134c92;
  --orange:#f28c1e;
  --ink:#1d1d1d;
  --body:#4a4a4a;
  --card:#f2f2f2;
  --footer:#f7f7f8;
  --hero:#141619;
  --white:#ffffff;
}
*{box-sizing:border-box;margin:0;padding:0}
html,body{width:1200px;height:3725px;overflow:hidden}
body{position:relative;background:var(--white);font-family:"Jost",sans-serif;color:var(--body)}
.abs{position:absolute}
.heading{font-family:"Poppins",sans-serif;font-weight:600;color:var(--blue);text-transform:uppercase}
.btn{position:absolute;display:flex;align-items:center;justify-content:center;background:var(--orange);color:var(--white);
  font-family:"Jost",sans-serif;font-weight:500;font-size:18px;text-transform:uppercase;border-radius:24px 0 24px 0;text-decoration:none}
.brand{display:flex;align-items:center;gap:14px;font-family:"Poppins",sans-serif;font-weight:700;color:var(--blue);letter-spacing:6px}
.brand-mark{width:34px;height:34px;background:var(--orange)}
.dot-icon{display:inline-block;width:22px;height:22px;border-radius:50%;background:var(--orange)}

/* header */
.site-header{position:absolute;left:0;top:0;width:1200px;height:111px}
.site-header .brand{left:29px;top:32px;font-size:46px;position:absolute}
.contact-bar{position:absolute;top:12px;left:410px;display:flex;gap:58px;font-size:18px;color:#333;align-items:center}
.contact-bar span{display:flex;align-items:center;gap:12px}
.header-social{position:absolute;top:15px;right:30px;display:flex;gap:30px}
.header-social .dot-icon{width:20px;height:20px}
.main-nav{position:absolute;left:334px;top:54px;width:866px;height:57px;background:var(--blue);border-radius:40px 0 0 0;
  display:flex;align-items:center;padding-left:48px;gap:0}
.main-nav a{color:var(--white);text-decoration:none;font-size:13.5px;text-transform:uppercase;margin-right:42px}
.main-nav .staff{margin:0;position:absolute;right:28px;top:14px;background:var(--orange);padding:7px 18px;border-radius:16px 0 16px 0;font-size:12.5px}

/* hero */
.hero{position:absolute;left:0;top:111px;width:1200px;height:629px;background:linear-gradient(120deg,#2a2e33 0%,var(--hero) 45%,#0e0f11 100%)}
.hero-copy .kicker{left:120px;top:185px;font-family:"Poppins",sans-serif;font-weight:600;color:var(--white);font-size:40px}
.hero-copy .big{left:116px;top:222px;font-family:"Poppins",sans-serif;font-weight:700;color:var(--blue);font-size:140px;line-height:1;font-style:normal}
.hero-copy .tail{left:120px;top:368px;font-family:"Poppins",sans-serif;font-weight:600;color:var(--white);font-size:40px}
.hero .btn{left:129px;top:444px;width:180px;height:50px}
.slider-dots{left:132px;top:587px;display:flex;gap:16px}
.slider-dots i{width:14px;height:14px;border-radius:50%;background:var(--blue);display:block}
.slider-dots i.on{background:var(--orange)}
.hero-ring{left:660px;top:82px}
.hero-product{left:785px;top:115px;width:280px;height:450px;border-radius:14px;background:linear-gradient(90deg,#cfd2d6,#f4f5f6 45%,#c4c7cb)}

/* story */
.story-frame{left:215px;top:856px;width:335px;height:309px;background:var(--orange)}
.story-photo{left:69px;top:885px;width:454px;height:402px;border-radius:70px 0 70px 0;background:linear-gradient(160deg,#d9d6d0,#8d8880 60%,#5f5b55)}
.story-title{left:600px;top:925px;font-size:34px}
.copy{font-size:19.5px;line-height:27.5px;font-weight:300;color:#4a4a4a}
.story-copy{left:600px;top:990px;width:540px}

/* compliance band */
.compliance{left:0;top:1404px;width:1200px;height:213px;background:var(--blue)}
.compliance h2{position:absolute;left:97px;top:68px;font-family:"Poppins",sans-serif;font-weight:500;color:var(--white);font-size:32px;line-height:39px}
.badge{position:absolute;top:47px;width:124px;height:124px;border-radius:50%}

/* offering */
.offer-title{left:0;width:1200px;top:1724px;text-align:center;font-size:34px}
.offer-sub{left:0;width:1200px;top:1782px;text-align:center;font-size:19px;font-weight:300}
.card{position:absolute;top:1871px;width:294px;height:406px;background:var(--card)}
.card .photo{width:294px;height:209px}
.card h3{position:absolute;top:265px;width:100%;text-align:center;font-family:"Poppins",sans-serif;font-weight:500;color:var(--ink);font-size:22px}
.card .btn{left:60px;top:331px;width:181px;height:50px}

/* heating */
.heat-title{left:75px;top:2512px;font-size:34px}
.heat-copy{left:75px;top:2578px;width:540px}
.heat-frame{left:638px;top:2431px;width:334px;height:309px;background:var(--orange)}
.heat-photo{left:665px;top:2454px;width:451px;height:403px;border-radius:70px 0 70px 0;background:linear-gradient(200deg,#e6e7e8,#b3b6b9 55%,#4f4c48)}

/* question */
.question{left:0;top:2989px;width:1200px;height:214px;background:linear-gradient(90deg,rgba(26,96,181,.93),rgba(32,104,190,.88)),linear-gradient(180deg,#4c6a8e,#2f4a6e)}
.question h2{position:absolute;left:0;width:100%;top:50px;text-align:center;font-family:"Poppins",sans-serif;font-weight:600;color:var(--white);font-size:38px}
.question p{position:absolute;left:0;width:100%;top:112px;text-align:center;font-family:"Poppins",sans-serif;font-weight:500;color:var(--orange);font-size:30px}

/* footer */
.site-footer{left:0;top:3203px;width:1200px;height:522px;background:var(--footer)}
.site-footer .brand{position:absolute;left:69px;top:84px;font-size:50px}
.footer-about{position:absolute;left:74px;top:175px;width:290px;font-size:19px;line-height:27.5px;font-weight:300;color:#555}
.footer-social{position:absolute;left:70px;top:340px;display:flex;gap:48px}
.footer-social .dot-icon{width:24px;height:24px}
.fcol{position:absolute;top:108px}
.fcol h4{font-family:"Poppins",sans-serif;font-weight:600;color:var(--orange);font-size:20px;text-transform:uppercase;margin-bottom:28px}
.fcol li{list-style:none;font-size:19px;line-height:25px;color:#444;margin-bottom:21px}
.news-text{font-size:18.5px;line-height:26px;color:#555;font-weight:300;width:235px}
.email{margin-top:22px;width:226px;height:50px;background:var(--white);padding-left:22px;display:flex;align-items:center;color:#888;font-size:19px}
.subscribe{width:226px;height:42px;background:var(--orange);color:var(--white);display:flex;align-items:center;justify-content:center;font-family:"Poppins",sans-serif;font-weight:500;font-size:19px;margin-top:4px}
.legal{position:absolute;top:466px;font-size:19px;color:#444}
</style>
</head>
<body>

<header class="site-header">
  <div class="brand"><span class="brand-mark"></span>OLVAK</div>
  <div class="contact-bar">
    <span><svg width="24" height="24" viewBox="0 0 24 24"><path d="M6.6 10.8a15 15 0 0 0 6.6 6.6l2.2-2.2c.3-.3.7-.4 1-.2 1.1.4 2.3.6 3.6.6.6 0 1 .4 1 1V20c0 .6-.4 1-1 1A17 17 0 0 1 3 4c0-.6.4-1 1-1h3.5c.6 0 1 .4 1 1 0 1.3.2 2.5.6 3.6.1.3 0 .7-.2 1z" fill="#f28c1e"/></svg>(+61)555 014 272</span>
    <span><svg width="26" height="22" viewBox="0 0 26 22"><rect x="1" y="5" width="24" height="16" rx="2" fill="#f28c1e"/><path d="M2 7l11 8 11-8" fill="none" stroke="#fff" stroke-width="2"/></svg>hello@olvak.example.au</span>
  </div>
  <div class="header-social">
    <span class="dot-icon" role="img" aria-label="Social link"></span>
    <span class="dot-icon" role="img" aria-label="Social link"></span>
    <span class="dot-icon" role="img" aria-label="Social link"></span>
  </div>
  <nav class="main-nav">
    <a href="#">Home</a><a href="#">Heating &amp; Cooling</a><a href="#">Our Story</a><a href="#">Support</a><a href="#">Book Appointment</a>
    <a class="staff" href="#">Staff Login</a>
  </nav>
</header>

<section class="hero" role="img" aria-label="Dark photo of a running shower head">
  <div class="hero-copy">
    <div class="abs kicker">SAVE UPTO</div>
    <div class="abs big">75%</div>
    <div class="abs tail">ELECTRICITY COST</div>
  </div>
  <a class="btn" href="#">Explore More</a>
  <div class="abs slider-dots"><i></i><i class="on"></i><i></i></div>
  <svg class="abs hero-ring" width="486" height="486" viewBox="0 0 486 486">
    <circle cx="243" cy="243" r="232" fill="none" stroke="#1a60b5" stroke-width="22"/>
    <circle cx="243" cy="243" r="190" fill="none" stroke="#f28c1e" stroke-width="62"/>
  </svg>
  <div class="abs hero-product" role="img" aria-label="Two white heat pump water heater units"></div>
</section>

<section>
  <div class="abs story-frame"></div>
  <div class="abs story-photo" role="img" aria-label="Room of modern home appliances"></div>
  <h2 class="abs heading story-title">Our Story</h2>
  <p class="abs copy story-copy">OLVAK is a company dedicated to manufacturing and installing energy-efficient products that reduce energy consumption, save costs, and promote sustainability. Our mission is to help individuals and businesses reduce their carbon footprint while also enhancing their comfort and quality of life.</p>
  <a class="btn" href="#" style="left:600px;top:1164px;width:181px;height:50px">Read More</a>
</section>

<section class="abs compliance">
  <h2>Fully Compliant with<br>all Government Rebates</h2>
  <span class="badge" role="img" aria-label="Locally owned badge" style="left:616px;background:#ffffff"></span>
  <span class="badge" role="img" aria-label="Premium quality badge" style="left:791px;background:#d8a32a"></span>
  <span class="badge" role="img" aria-label="Energy saving badge" style="left:955px;background:#ffffff"></span>
</section>

<section>
  <h2 class="abs heading offer-title">Offering Solutions For</h2>
  <p class="abs offer-sub">Please select from a category below that best suits your requirements.</p>
  <article class="card" style="left:113px">
    <div class="photo" role="img" aria-label="Home appliances in a living room" style="background:linear-gradient(160deg,#c9c4bd,#6e6862)"></div>
    <h3>Residential</h3><a class="btn" href="#">Read More</a>
  </article>
  <article class="card" style="left:460px">
    <div class="photo" role="img" aria-label="Technician working on pipes" style="background:linear-gradient(160deg,#e8eaec,#4a6fa0)"></div>
    <h3>Trade</h3><a class="btn" href="#">Read More</a>
  </article>
  <article class="card" style="left:805px">
    <div class="photo" role="img" aria-label="Commercial office building at dusk" style="background:linear-gradient(180deg,#6c7fb4,#b59a72 70%,#3d3a45)"></div>
    <h3>Commercial</h3><a class="btn" href="#">Read More</a>
  </article>
</section>

<section>
  <h2 class="abs heading heat-title">Heating &amp; Cooling</h2>
  <p class="abs copy heat-copy">OLVAK is a company dedicated to manufacturing and installing energy-efficient products that reduce energy consumption, save costs, and promote sustainability. Our mission is to help individuals and businesses reduce their carbon footprint while also enhancing their comfort and quality of life.</p>
  <a class="btn" href="#" style="left:74px;top:2752px;width:181px;height:50px">Read More</a>
  <div class="abs heat-frame"></div>
  <div class="abs heat-photo" role="img" aria-label="Technician servicing an outdoor air conditioning unit"></div>
</section>

<section class="abs question" role="img" aria-label="Faded living room with appliances behind blue overlay">
  <h2>HAVE A QUESTION?</h2>
  <p>Call : 1800 555 017</p>
</section>

<footer class="abs site-footer">
  <div class="brand"><span class="brand-mark"></span>OLVAK</div>
  <p class="footer-about">OLVAK is a company dedicated to manufacturing and installing energy-efficient products that reduce energy consumption, save costs, and promote sustainability.</p>
  <div class="footer-social">
    <span class="dot-icon" role="img" aria-label="Social link"></span>
    <span class="dot-icon" role="img" aria-label="Social link"></span>
    <span class="dot-icon" role="img" aria-label="Social link"></span>
  </div>
  <div class="fcol" style="left:438px">
    <h4>Our Products</h4>
    <ul><li>Heatpump</li><li>Air Conditioners</li><li>Swimming Pool Heat<br>Pumps</li><li>Monoblock Heat Pumps</li></ul>
  </div>
  <div class="fcol" style="left:698px">
    <h4>Useful Links</h4>
    <ul><li>Our Story</li><li>Support</li><li>Promotions</li><li>Appointment</li></ul>
  </div>
  <div class="fcol" style="left:931px">
    <h4>Stay Connected</h4>
    <p class="news-text">Enter your email address to register to our newsletter subscription</p>
    <div class="email">Email Address</div>
    <div class="subscribe">SUBSCRIBE NOW</div>
  </div>
  <p class="legal" style="left:69px">Copyright 2024 , All Rights Reserved</p>
  <p class="legal" style="right:54px">Privacy Policy | Terms &amp; Conditions</p>
</footer>

</body>
</html>
```